Product Label Design

Need a product design for our Epsom salt product, needs to have a luxurious simple feel to it. The picture attached is our brand and wordage on it, the bag we think should be a stand up bag that should be offwhite/creme color. The other picture are products that we like. We updated the packaging to be a Kraft tube box, please see the attached photo for dimensions.

```html
<!DOCTYPE html>
<html lang="en">
<head>
<meta charset="utf-8">
<title>HAVN Uplift – Epsom Salt Pouch</title>
<link href="https://fonts.googleapis.com/css2?family=Montserrat:wght@500;600;700;800&display=swap" rel="stylesheet">
<style>
  :root {
    --page: #ffffff;
    --creme: #e4dcc6;
    --creme-edge: #d9cfb5;
    --pattern-light: #e2d5b6;
    --pattern-gold: #d2b988;
    --bronze: #b67d38;
    --rule: #c99a5a;
    --ink: #333131;
  }
  * { margin: 0; padding: 0; box-sizing: border-box; }
  html, body {
    width: 1200px;
    height: 1200px;
    overflow: hidden;
    background: var(--page);
  }
  .canvas {
    position: relative;
    width: 1200px;
    height: 1200px;
    background: var(--page);
  }
  .pouch {
    position: absolute;
    left: 328px;
    top: 228px;
    width: 544px;
    height: 744px;
    background: var(--creme);
    border-radius: 10px;
    overflow: hidden;
    box-shadow: inset 0 0 0 10px var(--creme-edge);
    font-family: "Montserrat", sans-serif;
    color: var(--ink);
    text-align: center;
  }
  .pattern-band {
    position: absolute;
    left: 0;
    width: 100%;
  }
  .pattern-band--top {
    top: 0;
    height: 134px;
    background: linear-gradient(180deg, var(--pattern-light) 0%, var(--pattern-gold) 55%, var(--creme) 100%);
  }
  .pattern-band--bottom {
    bottom: 0;
    height: 140px;
    background: linear-gradient(0deg, var(--pattern-light) 0%, var(--pattern-gold) 55%, var(--creme) 100%);
  }
  .brand-name {
    position: absolute;
    top: 192px;
    left: 0;
    width: 100%;
    font-size: 96px;
    font-weight: 800;
    letter-spacing: 2px;
    line-height: 1;
    color: var(--bronze);
  }
  .variant {
    position: absolute;
    top: 312px;
    left: 0;
    width: 100%;
    font-size: 23px;
    font-weight: 700;
    letter-spacing: 0.5px;
  }
  .divider {
    position: absolute;
    top: 362px;
    left: 92px;
    width: 360px;
    height: 1px;
    background: var(--rule);
  }
  .ingredients {
    position: absolute;
    top: 398px;
    left: 0;
    width: 100%;
    font-size: 18px;
    line-height: 26px;
    font-weight: 500;
  }
  .ingredients .lead { font-weight: 700; }
  .net-weight {
    position: absolute;
    top: 570px;
    left: 0;
    width: 100%;
    font-size: 14px;
    font-weight: 700;
    letter-spacing: 0.3px;
  }
</style>
</head>
<body>
  <main class="canvas">
    <section class="pouch">
      <div class="pattern-band pattern-band--top" role="img" aria-label="Gold art deco pattern of diamonds with radiating fan lines"></div>

      <h1 class="brand-name">HAVN</h1>
      <p class="variant">UPLIFT</p>
      <div class="divider"></div>

      <p class="ingredients">
        <span class="lead">US Sourced Pure Epsom Salt</span><br>
        (Magnesium Sulfate)<br>
        + Abies sibirica<br>
        + Fir Balsam
      </p>

      <p class="net-weight">NET WT. 3LBS (1360g)</p>

      <div class="pattern-band pattern-band--bottom" role="img" aria-label="Gold art deco pattern of diamonds with radiating fan lines"></div>
    </section>
  </main>
</body>
</html>
```